Live Scavenger Hunt Mobile Platform needs a face lift!

We have been live for the past year and serving some very large customers, however, we are a group of developers that lack any real design skills. We are looking for a designer to help take our apps look and feel to the next level.

You can see the app in the Quellmart store here: https://apps.quellmart.example/us/app/trovanta.app/id913582047?mt=8

And in brindle pix here: https://shop.brindlepix.example/store/apps/developer?id=trovantaapp&hl=en

We do not plan to change the UX of app, but rather just the aesthetics. Ideally, if this project works out well we would work with the same designer to update our site: http://trovanta.app

You can watch a video of how the platform works here:
http://clipsharva.example/user8831054/elf-themed-christmas-scavenger-hunt

I have included the PSD files we used for the current mobile apps along with the PSD for our logo. In terms of colors we do like the current green and orange/red found in the logo. We have started to gravitate towards a brown textured background, but am open to change on this.

Industry/Entity Type

Store

Requirements
Must have
• The home screen should have a larger focus on getting started vs. the other three categories of 'hunts, settings and help'. We worked with a Marlowbrook designer when re-skinning the app for the experience an we liked how they did this.

https://apps.quellmart.example/us/app/pantry-quest/id730418855?mt=8
Nice to have
• - Custom web font (Some what playful) I am using Hobo Std in our logo
- Textured background
- Fun and playful, yet clean and clear. (Yes I realize that is a challenge)

```html
<!DOCTYPE html>
<html lang="en">
<head>
<meta charset="utf-8">
<title>Trovanta – Challenges Screen</title>
<link rel="stylesheet" href="https://fonts.googleapis.com/css2?family=Arimo:wght@400;700&family=Oswald:wght@600&display=swap">
<style>
  :root {
    --stage: #1d1e21;
    --header-dark: #6b3e12;
    --header-mid: #a8701f;
    --header-light: #c99a45;
    --tab-active-top: #d98a1c;
    --tab-active-bottom: #8a4608;
    --tab-idle-top: #6a3f12;
    --tab-idle-bottom: #2e1a07;
    --row-top: #f6f5f3;
    --row-bottom: #e3e1de;
    --row-divider: #b9aa98;
    --title-red: #9b0f0c;
    --points-grey: #8a8a8a;
    --chevron: #b8520f;
    --score-bg: #2d2b29;
    --white: #ffffff;
    --brand-text: #f4ead8;
  }
  * { box-sizing: border-box; margin: 0; padding: 0; }
  html, body { width: 1000px; height: 1200px; overflow: hidden; }
  body { background: var(--stage); font-family: "Arimo", Arial, sans-serif; position: relative; }

  .screen-label {
    position: absolute; left: 713px; top: 36px;
    font-family: "Oswald", "Arial Narrow", sans-serif; font-weight: 600;
    font-size: 46px; line-height: 48px; color: var(--white); letter-spacing: 1px;
  }

  .app-screen {
    position: absolute; left: 61px; top: 40px; width: 640px; height: 960px;
    overflow: hidden; background: var(--row-bottom);
  }

  .app-header {
    height: 88px; position: relative;
    background: radial-gradient(ellipse at 50% 40%, var(--header-light), var(--header-mid) 55%, var(--header-dark));
    display: flex; align-items: center; justify-content: center;
  }
  .brand-name { font-size: 46px; font-weight: 700; color: var(--brand-text); letter-spacing: 0.5px; }
  .header-button { position: absolute; top: 6px; width: 76px; height: 76px; }
  .header-button--back { left: 8px; }
  .header-button--settings { right: 8px; }

  .tab-bar { display: flex; height: 75px; }
  .tab {
    flex: 1; display: flex; align-items: center; justify-content: center;
    font-size: 32px; font-weight: 700; color: var(--white);
    border-radius: 8px 8px 0 0;
  }
  .tab--active { background: linear-gradient(var(--tab-active-top), var(--tab-active-bottom)); }
  .tab--idle { background: linear-gradient(var(--tab-idle-top), var(--tab-idle-bottom)); }

  .challenge-list { position: relative; list-style: none; }
  .list-backdrop {
    position: absolute; inset: 0;
    background: radial-gradient(ellipse at 30% 60%, rgba(214,190,150,0.35), transparent 60%);
    pointer-events: none;
  }
  .challenge-row {
    position: relative; height: 149px; padding: 32px 0 0 23px;
    background: linear-gradient(var(--row-top), var(--row-bottom));
    border-bottom: 1px solid var(--row-divider);
  }
  .challenge-title { font-size: 40px; font-weight: 700; color: var(--title-red); line-height: 44px; }
  .challenge-points { font-size: 28px; color: var(--points-grey); margin-top: 6px; }
  .row-chevron { position: absolute; left: 568px; top: 62px; width: 36px; height: 44px; }

  .score-tab {
    position: absolute; left: 246px; top: 905px; width: 150px; height: 60px;
    background: var(--score-bg); border-radius: 8px 8px 0 0;
    color: var(--white); font-size: 24px; text-align: center; padding-top: 16px;
  }
</style>
</head>
<body>
  <div class="screen-label">CHALLENGES<br>SCREEN</div>

  <main class="app-screen">
    <header class="app-header">
      <svg class="header-button header-button--back" viewBox="0 0 76 76" aria-label="Back">
        <circle cx="38" cy="38" r="34" fill="#8a4a16" stroke="#5a2c08" stroke-width="3"/>
        <path d="M50 30 H36 V22 L20 38 L36 54 V46 H50 Z" fill="#5a2c08"/>
      </svg>
      <span class="brand-name">Trovanta</span>
      <svg class="header-button header-button--settings" viewBox="0 0 76 76" aria-label="Settings">
        <circle cx="38" cy="38" r="34" fill="#8a4a16" stroke="#5a2c08" stroke-width="3"/>
        <circle cx="38" cy="38" r="14" fill="#5a2c08"/>
      </svg>
    </header>

    <nav class="tab-bar">
      <div class="tab tab--active">Challenges</div>
      <div class="tab tab--idle">Completed</div>
    </nav>

    <ul class="challenge-list">
      <li class="list-backdrop" role="img" aria-label="Soft sketched treasure-map scene with clouds behind the list"></li>
      <li class="challenge-row">
        <div class="challenge-title">Challenge name</div>
        <div class="challenge-points">10 point</div>
        <svg class="row-chevron" viewBox="0 0 36 44" aria-hidden="true">
          <path d="M4 2 L32 22 L4 42 L0 34 L18 22 L0 10 Z" fill="var(--chevron)"/>
        </svg>
      </li>
      <li class="challenge-row">
        <div class="challenge-title">Challenge name</div>
        <div class="challenge-points">10 point</div>
      </li>
      <li class="challenge-row">
        <div class="challenge-title">Challenge name</div>
        <div class="challenge-points">10 point</div>
      </li>
      <li class="challenge-row">
        <div class="challenge-title">Challenge name</div>
        <div class="challenge-points">10 point</div>
      </li>
      <li class="challenge-row">
        <div class="challenge-title">Challenge name</div>
        <div class="challenge-points">10 point</div>
      </li>
      <li class="challenge-row">
        <div class="challenge-title">Challenge name</div>
        <div class="challenge-points">10 point</div>
      </li>
    </ul>

    <div class="score-tab">Score</div>
  </main>
</body>
</html>
```